Criminal Defense law firm needs website and logo

Need a logo design and web design for a small firm in Miami, Florida. The firm concentrates in the areas of state and federal criminal defense in Miami Dade County, Florida.The firm handles cases in the areas of Drug Possession, Fraud Offenses, Traffic Offenses, domestic violence, Violent Crimes, probation violation, Juvenile Delinquency, and expunction/expungment of criminal records (detailed list provided in attachment). The name of the attorney is Loreta Benavides-Kurtz. Sole Practitioner. Will attach profile. (the attachment are from my previous law firm, can use any of the language but adjust to a sole practitioner)

Industry/Entity Type

Lawyer

Number of Pages Required

3 page

Font styles to use
Serif

Colors
0356a4

Requirements
Must have
• Page that includes area's of practice. Page for Attorney profile. Contact page indicating that we speak Spanish and accept all major credit cards.

```html
<!DOCTYPE html>
<html lang="en">
<head>
<meta charset="utf-8">
<title>Loreta Benavides-Kurtz — Criminal Defense</title>
<link rel="stylesheet" href="https://fonts.googleapis.com/css2?family=Raleway:wght@300;400;500;600&family=Open+Sans:wght@400;600;700&display=swap">
<style>
:root{
  --orange:#d8870c;
  --orange-soft:#eec98d;
  --ink:#2b2b2b;
  --grey-text:#555;
  --dark:#333333;
  --darker:#262626;
  --white:#ffffff;
  --ring:#d9d9d9;
}
*{box-sizing:border-box;margin:0;padding:0}
html,body{width:1200px;height:2258px;overflow:hidden}
body{position:relative;font-family:"Open Sans",Arial,sans-serif;background:var(--white);color:var(--ink)}
.abs{position:absolute}

/* header */
.site-header{position:absolute;left:0;top:0;width:1200px;height:107px;background:var(--white)}
.brand{position:absolute;left:54px;top:18px;display:flex;align-items:center;gap:10px}
.brand-mark{width:22px;height:22px;border-radius:50%;background:var(--orange)}
.brand-name{font-family:"Raleway",sans-serif;font-weight:600;font-size:17px;color:var(--orange);line-height:1.15;width:120px}
.main-nav a{position:absolute;top:46px;font-size:13.5px;color:#333;text-decoration:none;letter-spacing:.3px;text-transform:uppercase}
.main-nav a.active::after{content:"";position:absolute;left:0;right:0;top:24px;height:3px;background:var(--orange)}

/* hero */
.hero{position:absolute;left:0;top:107px;width:1200px;height:510px;
  background:radial-gradient(ellipse at 60% 45%,#5a4436 0%,#3b2a20 45%,#1f1611 100%)}
.hero-title{position:absolute;left:236px;top:234px;font-family:"Raleway",sans-serif;font-weight:300;font-size:118px;letter-spacing:7px;color:var(--orange);line-height:1}
.hero-sub{position:absolute;left:236px;top:364px;font-family:"Raleway",sans-serif;font-weight:500;font-size:43px;letter-spacing:3px;color:var(--white);line-height:1}
.slider-dots{position:absolute;left:1107px;top:268px;width:27px;height:146px;border-radius:14px;background:rgba(255,255,255,.3);display:flex;flex-direction:column;justify-content:space-evenly;align-items:center;padding:6px 0}
.slider-dots span{width:12px;height:12px;border-radius:50%;background:var(--white)}
.slider-dots span.current{background:var(--orange)}

/* welcome */
.welcome-title{position:absolute;left:0;top:664px;width:1200px;text-align:center;font-family:"Raleway",sans-serif;font-weight:400;font-size:36px;color:var(--ink)}
.welcome-title em{font-style:normal;color:var(--orange)}
.welcome-text{position:absolute;left:105px;top:730px;width:987px;text-align:center;font-size:12px;line-height:20px;color:var(--grey-text)}
.btn-read{position:absolute;left:535px;top:816px;width:122px;height:36px;background:var(--orange);color:var(--white);font-size:11px;text-transform:uppercase;display:flex;align-items:center;justify-content:center}

/* services */
.services{position:absolute;left:0;top:914px;width:1200px;height:1051px;background:var(--dark);overflow:hidden}
.services-photo{position:absolute;left:0;top:0;width:520px;height:1051px;
  background:linear-gradient(90deg,rgba(70,58,50,.55) 0%,rgba(60,52,46,.35) 60%,rgba(51,51,51,0) 100%)}
.services-title{position:absolute;left:0;top:38px;width:1200px;text-align:center;font-family:"Raleway",sans-serif;font-size:34px;color:var(--white)}
.services-title em{font-style:normal;color:var(--orange)}
.timeline{position:absolute;left:593px;top:110px;width:1px;height:866px;background:#6b6b6b}
.connector{position:absolute;height:1px;background:#6b6b6b}
.service-icon{position:absolute;width:116px;height:116px;border-radius:50%;background:var(--orange);border:4px solid var(--ring);box-shadow:0 0 0 2px rgba(255,255,255,.15);display:flex;align-items:center;justify-content:center}
.service-icon.active{background:#000;border-color:var(--orange)}
.service-icon svg{width:48px;height:48px}
.service{position:absolute;width:380px}
.service.left{text-align:right}
.service h3{font-size:19px;font-weight:600;color:var(--orange);line-height:24px}
.service.highlight h3{color:var(--white)}
.service p{margin-top:6px;font-size:11.5px;line-height:19.5px;color:var(--white)}
.service.highlight p{color:#c9c9c9}
.read-more{display:inline-block;margin-top:8px;font-size:11px;font-weight:700;color:var(--orange);text-transform:uppercase}
.service.highlight .read-more{color:var(--white)}
.read-more::after{content:"";display:inline-block;margin-left:7px;border-left:5px solid currentColor;border-top:4px solid transparent;border-bottom:4px solid transparent}

/* footer */
.site-footer{position:absolute;left:0;top:1965px;width:1200px;height:216px;background:var(--orange)}
.footer-heading{position:absolute;top:41px;font-size:16px;font-weight:700;color:var(--white);text-transform:uppercase}
.footer-links{position:absolute;left:57px;top:72px;list-style:none}
.footer-links li{height:28.5px;font-size:11px;color:var(--white);display:flex;align-items:center;gap:8px}
.footer-links li::before{content:"";width:11px;height:11px;border-radius:50%;border:1px solid var(--white);background:radial-gradient(circle,var(--white) 25%,transparent 30%)}
.field{position:absolute;width:157px;height:39px;background:var(--orange-soft);font-size:11px;font-style:italic;color:#a8824a;padding:12px 10px}
.btn-submit{position:absolute;left:259px;top:161px;width:131px;height:37px;background:var(--darker);color:var(--white);font-size:13px;display:flex;align-items:center;justify-content:center;text-transform:uppercase;border:1px solid #111}
.contact-lines{position:absolute;left:658px;top:72px;list-style:none}
.contact-lines li{height:28.5px;font-size:11px;color:var(--white);display:flex;align-items:center}
.contact-lines li.note{color:var(--ink)}
.social{position:absolute;top:89px;width:34px;height:34px;border-radius:50%;background:var(--white)}
.copyright{position:absolute;left:0;top:2181px;width:1200px;height:77px;background:var(--darker);color:var(--white);font-size:11px;padding:30px 50px}
</style>
</head>
<body>

<header class="site-header">
  <div class="brand"><span class="brand-mark"></span><span class="brand-name">Loreta Benavides-Kurtz</span></div>
  <nav class="main-nav">
    <a class="active" href="#" style="left:323px">Home</a>
    <a href="#" style="left:426px">About Us</a>
    <a href="#" style="left:552px">Area's of Practice</a>
    <a href="#" style="left:739px">Attorney Profile</a>
    <a href="#" style="left:920px">Testimonials</a>
    <a href="#" style="left:1072px">Contact Us</a>
  </nav>
</header>

<section class="hero" role="img" aria-label="Photograph of a wooden judge's gavel resting on a tax law book"></section>
<h1 class="hero-title">POWERFUL</h1>
<p class="hero-sub">PROTECTION OF MY CLIENTS</p>
<div class="slider-dots"><span></span><span></span><span></span><span class="current"></span><span></span></div>

<h2 class="welcome-title">Welcome to <em>Loreta Benavides-Kurtz</em></h2>
<p class="welcome-text">Lorem ipsum dolor sit amet, consectetur adipiscing elit, sed do eiusmod tempor incididunt ut labore et dolore magna aliqua. Ut enim ad minim veniam, quis nostrud exercitation ullamco laboris nisi ut aliquip ex ea commodo consequat. Duis aute irure dolor in reprehenderit in voluptate velit esse cillum dolore eu fugiat nulla pariatur. Excepteur sint occaecat cupidatat non proident, sunt in culpa qui officia deserunt mollit anim id est laborum.</p>
<a class="btn-read" href="#">Read More</a>

<section class="services">
  <div class="services-photo" role="img" aria-label="Bronze statue of Lady Justice holding scales"></div>
  <h2 class="services-title">Our <em>Service</em></h2>
  <div class="timeline"></div>

  <div class="connector" style="left:550px;top:267px;width:43px"></div>
  <div class="connector" style="left:550px;top:473px;width:43px"></div>
  <div class="connector" style="left:550px;top:731px;width:43px"></div>
  <div class="connector" style="left:593px;top:187px;width:48px"></div>
  <div class="connector" style="left:593px;top:369px;width:48px"></div>
  <div class="connector" style="left:593px;top:600px;width:48px"></div>
  <div class="connector" style="left:593px;top:848px;width:48px"></div>

  <!-- left icons -->
  <div class="service-icon" style="left:431px;top:209px"><svg viewBox="0 0 48 48" fill="none" stroke="#fff" stroke-width="3"><circle cx="24" cy="24" r="19"/><path d="M24 16l7 5-3 8h-8l-3-8z" fill="#fff"/></svg></div>
  <div class="service-icon" style="left:431px;top:415px"><svg viewBox="0 0 48 48" fill="none" stroke="#fff" stroke-width="5" stroke-linecap="round"><path d="M12 12l24 24M36 12L12 36"/><circle cx="24" cy="24" r="5" fill="#fff" stroke="none"/></svg></div>
  <div class="service-icon" style="left:431px;top:673px"><svg viewBox="0 0 48 48" fill="none" stroke="#fff" stroke-width="4" stroke-linecap="round"><path d="M19 8l-5 32M34 8l-5 32M9 18h32M7 31h32"/></svg></div>

  <!-- right icons -->
  <div class="service-icon active" style="left:641px;top:129px"><svg viewBox="0 0 48 48" fill="#fff"><rect x="16" y="6" width="14" height="22" rx="2" transform="rotate(45 23 17)"/><rect x="6" y="28" width="26" height="6" rx="3" transform="rotate(-45 19 31)"/></svg></div>
  <div class="service-icon" style="left:641px;top:311px"><svg viewBox="0 0 48 48" fill="none" stroke="#fff" stroke-width="3"><path d="M12 6h17l8 8v28H12z"/><path d="M18 22h13M18 28h13M18 34h13"/></svg></div>
  <div class="service-icon" style="left:641px;top:542px"><svg viewBox="0 0 48 48" fill="#fff"><path d="M20 10L6 22l14 12v-8c10 0 17 3 22 12-2-12-9-20-22-21z"/></svg></div>
  <div class="service-icon" style="left:641px;top:790px"><svg viewBox="0 0 48 48" fill="#fff"><path d="M28 4L14 27h9l-4 17 15-25h-9z"/></svg></div>

  <!-- left text -->
  <article class="service left" style="left:37px;top:210px">
    <h3>Traffic Offenses</h3>
    <p>We have worked with both large and small internet companies, and have grown companies to become market leaders in their sectors. We understand the inner workings</p>
    <span class="read-more">Read More</span>
  </article>
  <article class="service left" style="left:37px;top:416px">
    <h3>Domestic violence</h3>
    <p>Corvale Partners has key relationships in large web companies in Australia, the US, and the UK. These connections are critical to helping start the dialogue to create key</p>
    <span class="read-more">Read More</span>
  </article>
  <article class="service left" style="left:37px;top:675px">
    <h3>Probation violation</h3>
    <p>Corvale Partners strives to achieve the highest standard, and aligns with companies that pursue the same.</p>
    <span class="read-more" style="margin-top:26px">Read More</span>
  </article>

  <!-- right text -->
  <article class="service highlight" style="left:777px;top:132px">
    <h3>Drug Possession</h3>
    <p>Early stage companies have great ideas but often times cannot bootstrap themselves to profitability. Other companies have customers and revenue, but want to invest</p>
    <span class="read-more">Read More</span>
  </article>
  <article class="service" style="left:779px;top:312px">
    <h3>Fraud Offenses</h3>
    <p>We dedicate time on-site to our portfolio companies, and will arrange and attend key meetings with strategic partners or clients. Informal mentorship and advice through</p>
    <span class="read-more">Read More</span>
  </article>
  <article class="service" style="left:779px;top:544px">
    <h3>Violent Crimes</h3>
    <p>We have been on the buying side from big media companies and know how they evaluate and process acquisitions. We can help ensure that you build it the right way</p>
    <span class="read-more">Read More</span>
  </article>
  <article class="service" style="left:779px;top:789px">
    <h3>Juvenile Delinquency</h3>
    <p>We work as partners and align our interests to ensure the best outcome for all parties.</p>
    <span class="read-more" style="margin-top:26px">Read More</span>
  </article>
</section>

<footer class="site-footer">
  <h4 class="footer-heading" style="left:51px">About Us</h4>
  <ul class="footer-links">
    <li>Home</li><li>Area's of Practice</li><li>About Us</li><li>Testimonials</li><li>Attorney Profile</li>
  </ul>

  <h4 class="footer-heading" style="left:254px">Contact Us</h4>
  <div class="field" style="left:259px;top:70px">Name</div>
  <div class="field" style="left:420px;top:70px">Phone</div>
  <div class="field" style="left:259px;top:113px">E-mail</div>
  <div class="field" style="left:420px;top:113px">Message</div>
  <div class="btn-submit">Submit</div>

  <h4 class="footer-heading" style="left:655px">Have Questions?</h4>
  <ul class="contact-lines">
    <li>123-456-7890</li><li>info@benavideskurtz-law.com</li><li class="note">Lorem Ipsum is simply dummy</li>
  </ul>

  <h4 class="footer-heading" style="left:949px">Follow Us</h4>
  <span class="social" style="left:945px"></span>
  <span class="social" style="left:990px"></span>
  <span class="social" style="left:1036px"></span>
  <span class="social" style="left:1082px"></span>
</footer>
<div class="copyright">Copy Right @ 2015 Loreta Benavides-Kurtz.All Rights Reserved</div>

</body>
</html>
```